Christmas and New Year wishes

I would like to send as a picture in a email a graphic that relates to:
-thanks for the collaboration / partnership in the past year (to be used for customers and partners)
-Wishes for Merry christmas and a successful 2019
-it should be colored and possibly include our logo color (www.velkarin.ch) (nice to have), or the name of our company

Target Market(s)

Customers and partners

Industry/Entity Type

It Company

Font styles to use
Sans Serif

Colors
9bcb3c
0455a3

Requirements
Must have
• Relation to christmas
• Relation to New year
Nice to have
• The colors below are near to the company logo color. But feel free to use any other logo
• a funny design
• Happy Customer or partner (supplier)
• Can be a mixture of text and drawing

```html
<!DOCTYPE html>
<html lang="en">
<head>
<meta charset="utf-8">
<title>Season's Greetings – Velkarin</title>
<link rel="stylesheet" href="https://fonts.googleapis.com/css2?family=Elsie+Swash+Caps:wght@400;900&family=Montserrat:wght@300;500;600&display=swap">
<style>
  :root {
    --navy: #02101d;
    --steel: #4a7190;
    --lime: #c2f536;
    --green: #95c705;
    --ring-blue: #255d83;
    --white: #ffffff;
    --logo-grey: #5b7a90;
    --snow-light: #e9ecef;
    --snow-mid: #b9bfc6;
    --portrait-light: #d9d4cd;
    --portrait-mid: #a89e93;
    --gift-blue: #1e8fc0;
    --gift-pink: #c978c8;
    --gift-dark: #2a1540;
  }
  * { box-sizing: border-box; margin: 0; padding: 0; }
  html, body { width: 1200px; height: 869px; overflow: hidden; background: var(--steel); }
  .card { position: relative; width: 1200px; height: 869px; background: var(--steel); overflow: hidden; }

  .year-panel { position: absolute; left: 0; top: 0; width: 506px; height: 869px; background: var(--navy); overflow: hidden; }
  .year-panel svg { position: absolute; inset: 0; }
  .brand {
    position: absolute; left: 19px; top: 806px;
    font-family: "Montserrat", sans-serif; font-weight: 300;
    font-size: 34px; letter-spacing: 0.5px; color: var(--logo-grey);
    text-transform: lowercase;
  }

  .photo { position: absolute; }
  .photo--snowman { left: 529px; top: 0; width: 306px; height: 298px;
    background: radial-gradient(circle at 55% 45%, var(--white) 0 22%, var(--snow-mid) 50%, var(--snow-light) 100%); }
  .photo--portrait { left: 855px; top: 0; width: 345px; height: 298px;
    background: linear-gradient(160deg, var(--portrait-light), var(--portrait-mid)); }
  .photo--gifts { left: 528px; top: 586px; width: 672px; height: 283px;
    background: linear-gradient(120deg, var(--gift-dark) 0%, var(--gift-blue) 40%, var(--gift-pink) 75%, var(--gift-dark) 100%); }

  .dot-row { position: absolute; left: 538px; width: 646px; height: 18px; }
  .dot-row--top { top: 308px; }
  .dot-row--bottom { top: 558px; }

  .greeting { position: absolute; inset: 0; pointer-events: none; }
  .greeting__line { position: absolute; white-space: nowrap; }
  .greeting__intro { left: 592px; top: 332px; font-family: "Montserrat", sans-serif; font-weight: 500; font-size: 31px; color: var(--white); }
  .greeting__christmas {
    left: 629px; top: 354px;
    font-family: "Elsie Swash Caps", serif; font-weight: 400; font-size: 86px; color: var(--lime);
    transform: scaleX(0.65); transform-origin: left top;
  }
  .greeting__bridge { left: 804px; top: 438px; font-family: "Montserrat", sans-serif; font-weight: 500; font-size: 30px; color: var(--white); }
  .greeting__newyear {
    left: 655px; top: 461px;
    font-family: "Elsie Swash Caps", serif; font-weight: 400; font-size: 86px; color: var(--lime);
    transform: scaleX(0.74); transform-origin: left top;
  }
</style>
</head>
<body>
<main class="card">
  <section class="year-panel" aria-label="2018">
    <svg width="506" height="869" viewBox="0 0 506 869" aria-hidden="true">
      <g class="digit-eight" fill="none" stroke="var(--ring-blue)" stroke-width="30">
        <ellipse cx="320" cy="460" rx="95" ry="92"/>
        <ellipse cx="318" cy="700" rx="152" ry="135"/>
      </g>
      <text class="digit-two" x="-18" y="482" font-family="Montserrat, sans-serif" font-weight="300" font-size="660" fill="var(--lime)">2</text>
      <ellipse class="digit-zero" cx="360" cy="316" rx="155" ry="248" transform="rotate(-6 360 316)" fill="none" stroke="var(--green)" stroke-width="38"/>
      <path class="digit-one" fill="var(--white)" d="M78 207 H199 V568 H269 V599 H54 V568 H127 V237 H78 Z"/>
    </svg>
    <div class="brand">velkarin</div>
  </section>

  <div class="photo photo--snowman" role="img" aria-label="Photo of a small snowman with a top hat and lime scarf in the snow"></div>
  <div class="photo photo--portrait" role="img" aria-label="Photo of a smiling customer"></div>

  <svg class="dot-row dot-row--top" viewBox="0 0 646 18" aria-hidden="true">
    <g fill="var(--white)">
      <circle cx="9" cy="9" r="9"/><circle cx="32.4" cy="9" r="9"/><circle cx="55.8" cy="9" r="9"/><circle cx="79.2" cy="9" r="9"/><circle cx="102.6" cy="9" r="9"/><circle cx="126" cy="9" r="9"/><circle cx="149.4" cy="9" r="9"/><circle cx="172.8" cy="9" r="9"/><circle cx="196.2" cy="9" r="9"/><circle cx="219.6" cy="9" r="9"/><circle cx="243" cy="9" r="9"/><circle cx="266.4" cy="9" r="9"/><circle cx="289.8" cy="9" r="9"/><circle cx="313.2" cy="9" r="9"/><circle cx="336.6" cy="9" r="9"/><circle cx="360" cy="9" r="9"/><circle cx="383.4" cy="9" r="9"/><circle cx="406.8" cy="9" r="9"/><circle cx="430.2" cy="9" r="9"/><circle cx="453.6" cy="9" r="9"/><circle cx="477" cy="9" r="9"/><circle cx="500.4" cy="9" r="9"/><circle cx="523.8" cy="9" r="9"/><circle cx="547.2" cy="9" r="9"/><circle cx="570.6" cy="9" r="9"/><circle cx="594" cy="9" r="9"/><circle cx="617.4" cy="9" r="9"/><circle cx="637" cy="9" r="9"/>
    </g>
  </svg>

  <div class="greeting">
    <p class="greeting__line greeting__intro">Wishing you a</p>
    <p class="greeting__line greeting__christmas">Merry Christmas</p>
    <p class="greeting__line greeting__bridge">&amp; a Wonderful</p>
    <p class="greeting__line greeting__newyear">New Year</p>
  </div>

  <svg class="dot-row dot-row--bottom" viewBox="0 0 646 18" aria-hidden="true">
    <g fill="var(--white)">
      <circle cx="9" cy="9" r="9"/><circle cx="32.4" cy="9" r="9"/><circle cx="55.8" cy="9" r="9"/><circle cx="79.2" cy="9" r="9"/><circle cx="102.6" cy="9" r="9"/><circle cx="126" cy="9" r="9"/><circle cx="149.4" cy="9" r="9"/><circle cx="172.8" cy="9" r="9"/><circle cx="196.2" cy="9" r="9"/><circle cx="219.6" cy="9" r="9"/><circle cx="243" cy="9" r="9"/><circle cx="266.4" cy="9" r="9"/><circle cx="289.8" cy="9" r="9"/><circle cx="313.2" cy="9" r="9"/><circle cx="336.6" cy="9" r="9"/><circle cx="360" cy="9" r="9"/><circle cx="383.4" cy="9" r="9"/><circle cx="406.8" cy="9" r="9"/><circle cx="430.2" cy="9" r="9"/><circle cx="453.6" cy="9" r="9"/><circle cx="477" cy="9" r="9"/><circle cx="500.4" cy="9" r="9"/><circle cx="523.8" cy="9" r="9"/><circle cx="547.2" cy="9" r="9"/><circle cx="570.6" cy="9" r="9"/><circle cx="594" cy="9" r="9"/><circle cx="617.4" cy="9" r="9"/><circle cx="637" cy="9" r="9"/>
    </g>
  </svg>

  <div class="photo photo--gifts" role="img" aria-label="Photo of wrapped gift boxes in blue and pink with ribbons"></div>
</main>
</body>
</html>
```